Financial Planning business needs a new Business Card design

We need a business card design for an Australian financial planning business. I am looking for a clean simple design

Target Market(s)

People aged 25-40

Industry/Entity Type

Financial Service

Contact Information for Business Card

On the front of the card we need the following information:
Name: Colin Merrow (First Name Green: #006838 and last name Grey: #414042)
Position: Financial Adviser
Qualifications: BEc(Hons), AdDipFS(FP), Dip FMBM, CFL®
Mobile: 0437 512 604
Email: colin@brightledgeplan.com.au

On the back of the card we need:
Postal address: PO BOX 5307, PERTH BC, WA 6849
Website: www.brightledgeplan.com.au
Text: AFS Licence No. 518760

The fields need to be able to be edited.

Font styles to use
Sans Serif

Requirements
Must have
• Information listed above

```html
<!DOCTYPE html>
<html lang="en">
<head>
<meta charset="utf-8">
<title>Brightledge Plan – Business Card</title>
<link rel="stylesheet" href="https://fonts.googleapis.com/css2?family=Montserrat:wght@400;700;800&display=swap">
<style>
  :root {
    --brand-green: #006838;
    --brand-grey: #414042;
    --card-border: #9a9a9a;
    --canvas: #ffffff;
    --mark-faint: #2f8158;
    --text-light: #ffffff;
  }
  * { margin: 0; padding: 0; box-sizing: border-box; }
  html, body {
    width: 1200px;
    height: 1000px;
    overflow: hidden;
    background: var(--canvas);
    font-family: "Montserrat", "Helvetica Neue", Arial, sans-serif;
  }
  .canvas { position: relative; width: 1200px; height: 1000px; }

  .card { position: absolute; left: 271px; width: 658px; height: 379px; }
  .card--front { top: 84px; background: #fff; border: 1px solid var(--card-border); }
  .card--back { top: 537px; background: var(--brand-green); }

  .wordmark {
    position: absolute;
    font-weight: 800;
    text-transform: uppercase;
    letter-spacing: 0.5px;
    white-space: nowrap;
  }
  .card--front .wordmark {
    right: 38px;
    top: 140px;
    font-size: 36px;
    color: var(--brand-green);
  }
  .card--back .wordmark {
    left: 0; right: 0;
    top: 128px;
    text-align: center;
    font-size: 52px;
    color: var(--mark-faint);
  }

  .contact { position: absolute; left: 38px; top: 228px; color: var(--brand-grey); }
  .contact__name { font-size: 22px; font-weight: 700; line-height: 28px; }
  .contact__first { color: var(--brand-green); }
  .contact__last { color: var(--brand-grey); }
  .contact__role,
  .contact__quals { font-size: 16px; line-height: 20px; }
  .contact__quals sup { font-size: 9px; vertical-align: 6px; }
  .contact__line { font-size: 19px; line-height: 24px; }

  .back-details {
    position: absolute;
    left: 0; right: 0;
    top: 275px;
    text-align: center;
    color: var(--text-light);
    font-size: 19px;
    line-height: 24px;
  }
</style>
</head>
<body>
<main class="canvas">
  <section class="card card--front" aria-label="Business card front">
    <div class="wordmark">Brightledge Plan</div>
    <div class="contact">
      <p class="contact__name"><span class="contact__first">Colin</span> <span class="contact__last">Merrow</span></p>
      <p class="contact__role">Financial Adviser</p>
      <p class="contact__quals">BEc(Hons), AdDipFS(FP), Dip FMBM, CFL<sup>®</sup></p>
      <p class="contact__line">M: 0437 512 604</p>
      <p class="contact__line">E: colin@brightledgeplan.com.au</p>
    </div>
  </section>

  <section class="card card--back" aria-label="Business card back">
    <div class="wordmark">Brightledge Plan</div>
    <div class="back-details">
      <p>Add: PO BOX 5307, PERTH BC, WA 6849</p>
      <p>www.brightledgeplan.com.au</p>
      <p>AFS Licence No. 518760</p>
    </div>
  </section>
</main>
</body>
</html>
```